Torvel Law, PC Letterhead Design -- LAW FIRM

I am looking for a very elegant letterhead design for my personal injury law practice.
The letter head must have 4 different variations of the same thing meaning one design that has just a header, and another with a header and footer.
Elegance is key, I do not want it to be too bold. Please stay away from colors that are not black, white or gray or silver.
Please include a gradient style letterhead for the header while implementing the design of the logo found in folder #3
I have attached for you the logos and emblems for my company below.
In folders 1-4 you will find my actual logo.
In folder 5-6 you will find a shorter version of my logo, this can be implemented maybe in the footer + header design of the letter head (do not include this shortened version in the header).
In folders 7-8 you will find an emblem for my company.
Information that needs to be found on the letterhead is as follows:
A clearly written version of my company name: Torvel Law, PC
Address: 4718 Pemberly Avenue Suite #512, Ashford Glen, CA, 90412
Email: dorian@torvellaw.example
Telephone number: 310-555-0174

```html
<!DOCTYPE html>
<html lang="en">
<head>
<meta charset="utf-8">
<title>Torvel Law, PC — Letterhead</title>
<link href="https://fonts.googleapis.com/css2?family=Montserrat:ital,wght@0,400;0,600;0,700;1,400&display=swap" rel="stylesheet">
<style>
  :root {
    --backdrop: #4b4b4b;
    --paper: #ffffff;
    --ink: #3b3b3b;
    --mark: #2f2a29;
    --band: #8c8c8c;
    --band-text: #ffffff;
    --signature-tone: #d9d9d9;
  }
  * { margin: 0; padding: 0; box-sizing: border-box; }
  html, body {
    width: 1200px; height: 908px; overflow: hidden;
    background: var(--backdrop);
    font-family: "Montserrat", sans-serif;
    color: var(--ink);
  }
  .canvas { position: relative; width: 1200px; height: 908px; }
  .sheet {
    position: absolute; width: 378px; height: 489px;
    background: var(--paper); overflow: hidden;
  }
  .sheet--blank { left: 111px; top: 66px; }
  .sheet--letter { left: 607px; top: 349px; }

  .brand-head {
    position: absolute; left: 0; right: 0; top: 26px;
    text-align: center; font-weight: 600; font-size: 11px;
    letter-spacing: 0.6px; color: var(--mark);
  }

  .footer-band { position: absolute; left: 0; bottom: 0; width: 378px; height: 63px; }
  .footer-band svg.curve { position: absolute; left: 0; top: 0; }
  .footer-name {
    position: absolute; left: 0; right: 0; top: 9px;
    text-align: center; font-weight: 600; font-size: 9px;
    letter-spacing: 0.5px; color: var(--band-text);
  }
  .contact-line {
    position: absolute; left: 0; right: 0; top: 37px;
    display: flex; justify-content: center; gap: 7px;
    font-size: 5.6px; color: var(--band-text); white-space: nowrap;
  }
  .contact-item { display: flex; align-items: center; gap: 2.5px; }
  .contact-item svg { width: 6px; height: 6px; }

  .letter-date { position: absolute; left: 52px; top: 102px; font-size: 7px; font-weight: 700; }
  .recipient { position: absolute; left: 52px; top: 128px; font-size: 6.8px; line-height: 9.4px; }
  .recipient .name { font-weight: 700; }
  .recipient .role { font-style: italic; }
  .letter-body { position: absolute; left: 52px; top: 175px; width: 276px; font-size: 7px; line-height: 10.3px; }
  .letter-body p { margin-bottom: 8.2px; }
  .sign-off { position: absolute; right: 51px; top: 326px; font-size: 6.8px; text-align: right; }
  .signature-area {
    position: absolute; left: 266px; top: 340px; width: 64px; height: 19px;
    background: linear-gradient(90deg, var(--signature-tone), #efefef);
    border-radius: 2px;
  }
  .signer { position: absolute; left: 272px; top: 357px; width: 58px; text-align: center; font-size: 7px; font-weight: 700; }
</style>
</head>
<body>
<main class="canvas">

  <section class="sheet sheet--blank" aria-label="Letterhead, blank">
    <div class="brand-head">Torvel Law, PC</div>
    <footer class="footer-band">
      <svg class="curve" width="378" height="63" viewBox="0 0 378 63"><path d="M0 20 Q189 -20 378 20 V63 H0 Z" fill="var(--band)"/></svg>
      <div class="footer-name">Torvel Law, PC</div>
      <div class="contact-line">
        <span class="contact-item"><svg viewBox="0 0 10 10"><path d="M5 0.5a3.3 3.3 0 0 0-3.3 3.3C1.7 6.3 5 9.5 5 9.5s3.3-3.2 3.3-5.7A3.3 3.3 0 0 0 5 0.5z" fill="#fff"/><circle cx="5" cy="3.8" r="1.2" fill="var(--band)"/></svg>4718 Pemberly Avenue Suite #512, Ashford Glen, CA, 90412</span>
        <span class="contact-item"><svg viewBox="0 0 10 10"><circle cx="5" cy="5" r="4.6" fill="#fff"/><rect x="2.6" y="3.4" width="4.8" height="3.2" fill="var(--band)"/></svg>dorian@torvellaw.example</span>
        <span class="contact-item"><svg viewBox="0 0 10 10"><circle cx="5" cy="5" r="4.6" fill="#fff"/><path d="M3.4 2.6l1 1-0.6 0.8c0.4 0.8 1 1.4 1.8 1.8l0.8-0.6 1 1-0.7 0.9C4.9 7.3 2.7 5.1 2.5 3.3z" fill="var(--band)"/></svg>310-555-0174</span>
      </div>
    </footer>
  </section>

  <section class="sheet sheet--letter" aria-label="Letterhead, sample letter">
    <div class="brand-head">Torvel Law, PC</div>

    <p class="letter-date">Date, 22 February 2022</p>
    <div class="recipient">
      <p>To:</p>
      <p class="name">Marcus Hale</p>
      <p class="role">Chief Officer</p>
    </div>
    <div class="letter-body">
      <p>Lorem ipsum dolor sit amet, consectetur adipiscing elit. Duis auctor sem vel metus interdum porta. Duis consequat bibendum felis eget cursus. Nulla eget purus vehicula ipsum finibus egestas. Nullam ligula ipsum, mollis sed gravida vitae, maximus eu dolor. Morbi luctus sem a congue consectetur.</p>
      <p>Orci varius natoque penatibus et magnis dis parturient montes, nascetur ridiculus mus. Vestibulum congue eros auctor, ullamcorper libero blandit, tempor tellus. Proin vitae tellus et nunc fringilla lacinia. Sed augue erat, facilisis laoreet velit a, convallis mattis nunc. Nunc sagittis ligula vitae sollicitudin sollicitudin.</p>
      <p>Nulla facilisi. Nulla quis odio vitae purus aliquam fermentum ut nec diam. Fusce sed velit ultrices, aliquam augue ut, sollicitudin orci.</p>
    </div>
    <p class="sign-off">Kind Regards</p>
    <div class="signature-area" role="img" aria-label="Handwritten signature"></div>
    <p class="signer">Marcus Hale</p>

    <footer class="footer-band">
      <svg class="curve" width="378" height="63" viewBox="0 0 378 63"><path d="M0 20 Q189 -20 378 20 V63 H0 Z" fill="var(--band)"/></svg>
      <div class="footer-name">Torvel Law, PC</div>
      <div class="contact-line">
        <span class="contact-item"><svg viewBox="0 0 10 10"><path d="M5 0.5a3.3 3.3 0 0 0-3.3 3.3C1.7 6.3 5 9.5 5 9.5s3.3-3.2 3.3-5.7A3.3 3.3 0 0 0 5 0.5z" fill="#fff"/><circle cx="5" cy="3.8" r="1.2" fill="var(--band)"/></svg>4718 Pemberly Avenue Suite #512, Ashford Glen, CA, 90412</span>
        <span class="contact-item"><svg viewBox="0 0 10 10"><circle cx="5" cy="5" r="4.6" fill="#fff"/><rect x="2.6" y="3.4" width="4.8" height="3.2" fill="var(--band)"/></svg>dorian@torvellaw.example</span>
        <span class="contact-item"><svg viewBox="0 0 10 10"><circle cx="5" cy="5" r="4.6" fill="#fff"/><path d="M3.4 2.6l1 1-0.6 0.8c0.4 0.8 1 1.4 1.8 1.8l0.8-0.6 1 1-0.7 0.9C4.9 7.3 2.7 5.1 2.5 3.3z" fill="var(--band)"/></svg>310-555-0174</span>
      </div>
    </footer>
  </section>

</main>
</body>
</html>
```